OpenCart website

We have an existing site that was based on open cart in 2011 but customised heavily. We want a brand new open cart site designed from scratch so we can work on transitioning the existing opencart database over after the project is done

Current site: www.quillfernstores.com

```html
<!DOCTYPE html>
<html lang="en">
<head>
<meta charset="utf-8">
<title>Quillfern Stores</title>
<link rel="stylesheet" href="https://fonts.googleapis.com/css2?family=Open+Sans:wght@400;600;700&family=Cinzel:wght@400;700&display=swap">
<style>
:root{
  --frame:#e6e6e6;
  --page:#ffffff;
  --band:#efefef;
  --ink:#1a1a1a;
  --nav:#555555;
  --body:#6a6a6a;
  --card:#0b0b0b;
  --card-row:#1c1c1c;
  --line:#c8c8c8;
  --pager:#c9c9c9;
  --pager-active:#555555;
  --bar:#1b1b1b;
}
*{margin:0;padding:0;box-sizing:border-box}
html,body{width:1200px;height:2314px;overflow:hidden}
body{background:var(--frame);font-family:"Open Sans",Arial,sans-serif;color:var(--ink);position:relative}
.page{position:absolute;left:14px;top:14px;width:1172px;height:2286px;background:var(--page);overflow:hidden}
.abs{position:absolute}

.brand{left:88px;top:46px;font-weight:700;font-size:27px;line-height:30px;color:#333;letter-spacing:.5px}
.social{left:1007px;top:74px;display:flex;gap:4px}
.social span{width:24px;height:24px;border:1.5px solid #777;border-radius:50%}

.nav{top:184px;left:0;width:100%;font-size:14px;font-weight:700;color:var(--nav);text-transform:uppercase}
.nav a{position:absolute;color:inherit;text-decoration:none;white-space:nowrap}
.nav a.active{color:var(--ink)}

.hero{left:88px;top:203px;width:996px;height:508px;background:#fff;border:1px solid #ddd;border-radius:6px;padding:5px;box-shadow:0 10px 14px -8px rgba(0,0,0,.3)}
.hero div{width:100%;height:100%;border-radius:4px;background:linear-gradient(100deg,#e9e6e2 0%,#c9b7a5 30%,#9a9a98 55%,#d8c7a6 80%,#e7e3dd 100%)}

.section-title{left:0;width:100%;text-align:center;font-weight:700;font-size:18px;text-transform:uppercase}

.news{top:885px;width:315px}
.news .photo{height:187px;border-radius:6px;box-shadow:0 8px 10px -6px rgba(0,0,0,.35)}
.news h3{font-family:"Cinzel",Georgia,serif;font-weight:700;font-size:16px;line-height:22px;margin-top:20px;color:#222}
.news p{font-size:12.5px;line-height:19.6px;color:var(--body);margin-top:13px}
.news .more{margin-top:12px;width:24px;height:24px;border-radius:50%;background:#8a8a8a;border:2px solid #d0d0d0;display:flex;align-items:center;justify-content:center}

.band{left:0;top:1402px;width:100%;height:668px;background:var(--band)}
.tab{top:1542px;width:292px;height:45px;font-family:"Cinzel",Georgia,serif;font-size:16px;display:flex;align-items:center;justify-content:center;border-radius:4px 4px 0 0}
.tab.on{background:#333;color:#fff}
.tab.off{background:#fff;color:#222;border:1px solid #ddd;border-bottom:none}
.tab-rule{left:88px;top:1586px;width:996px;height:2px;background:var(--line)}

.product{top:1624px;width:236px;height:250px;background:var(--card);border-radius:4px;overflow:hidden;box-shadow:0 10px 12px -6px rgba(0,0,0,.35);color:#fff}
.product .photo{height:159px}
.product .name{height:46px;padding:0 16px;display:flex;align-items:center;font-size:13px;color:#e8e8e8}
.product .row{height:45px;background:var(--card-row);display:flex;justify-content:space-between;align-items:center;padding:0 14px;font-size:12.5px;font-weight:700}
.product .row span{display:flex;align-items:center;gap:7px}
.ico{width:18px;height:18px;border:1.3px solid #bbb;border-radius:50%;font-size:9px;display:flex;align-items:center;justify-content:center;font-weight:400}

.pager{left:435px;top:1922px;display:flex;border-radius:5px;overflow:hidden;background:var(--pager)}
.pager span{width:27.5px;height:26px;display:flex;align-items:center;justify-content:center;font-size:14px;font-weight:700;color:#333;border-right:1px solid #e4e4e4}
.pager span.on{background:var(--pager-active);color:#fff}
.pager span.arrow{color:#888;font-weight:400}
.pager span:last-child{border-right:none}

.foot-tab{left:0;top:2010px}
.foot-brand{left:0;width:100%;top:2052px;text-align:center;font-weight:700;font-size:27px;line-height:30px;color:#333}
.foot-rule{left:261px;top:2174px;width:650px;height:2px;background:linear-gradient(90deg,transparent,#444 15%,#444 85%,transparent)}
.foot-nav{top:2194px;left:0;width:100%;font-size:13px;font-weight:700;color:var(--nav)}
.foot-nav a{position:absolute;color:inherit;text-decoration:none;white-space:nowrap}
.bar{left:0;top:2253px;width:100%;height:28px;background:var(--bar);color:#fff;font-size:9.5px;font-weight:700;display:flex;justify-content:space-between;align-items:center;padding:0 30px}
</style>
</head>
<body>
<div class="page">

  <div class="abs brand">QUILLFERN<br>STORES</div>
  <div class="abs social" aria-label="Social links"><span></span><span></span><span></span></div>

  <nav class="abs nav">
    <a class="active" style="left:222px">Home</a>
    <a style="left:315px">Shop by Brand</a>
    <a style="left:478px">Latest Promotion</a>
    <a style="left:669px">Events</a>
    <a style="left:771px">News</a>
    <a style="left:862px">Contact Us</a>
  </nav>

  <div class="abs hero"><div role="img" aria-label="Couple preparing a meal together in a bright home kitchen"></div></div>

  <h2 class="abs section-title" style="top:812px">What's happening at Quillfern Stores</h2>

  <article class="abs news" style="left:91px">
    <div class="photo" role="img" aria-label="Vegetables being stir-fried in a wok" style="background:linear-gradient(120deg,#e9e7e5,#8a5a3a 45%,#3d556e)"></div>
    <h3>News #1<br>November 10, 2016</h3>
    <p>Lorem ipsum dolor sit amet, consectetuer adipiscing elit, sed diam nonummy nibh euismod tincidunt ut laoreet dolore magna aliquam erat volutpat. Ut wisi enim ad minim veniam, quis nostrud exerci tation ullamcorper suscipit lobortis nisl ut aliquip ex ea commodo consequat.</p>
    <div class="more"><svg width="12" height="12" viewBox="0 0 12 12"><path d="M2 6h7M6 3l3 3-3 3" stroke="#fff" stroke-width="1.8" fill="none"/></svg></div>
  </article>

  <article class="abs news" style="left:427px">
    <div class="photo" role="img" aria-label="Kitchen utensils and wooden cutting boards" style="background:linear-gradient(120deg,#5d6b75,#3c3a38 45%,#c8a67c)"></div>
    <h3>News #2<br>November 8, 2016</h3>
    <p>Lorem ipsum dolor sit amet, consectetuer adipiscing elit, sed diam nonummy nibh euismod tincidunt ut laoreet dolore magna aliquam erat volutpat. Ut wisi enim ad minim veniam, quis nostrud exerci tation ullamcorper suscipit lobortis nisl ut aliquip ex ea commodo consequat.</p>
    <div class="more"><svg width="12" height="12" viewBox="0 0 12 12"><path d="M2 6h7M6 3l3 3-3 3" stroke="#fff" stroke-width="1.8" fill="none"/></svg></div>
  </article>

  <article class="abs news" style="left:765px">
    <div class="photo" role="img" aria-label="Hands cutting cookie dough with star cutters" style="background:linear-gradient(120deg,#2e2e30,#6b4c3b 50%,#3a3633)"></div>
    <h3>News #3<br>November 2, 2016</h3>
    <p>Lorem ipsum dolor sit amet, consectetuer adipiscing elit, sed diam nonummy nibh euismod tincidunt ut laoreet dolore magna aliquam erat volutpat. Ut wisi enim ad minim veniam, quis nostrud exerci tation ullamcorper suscipit lobortis nisl ut aliquip ex ea commodo consequat.</p>
    <div class="more"><svg width="12" height="12" viewBox="0 0 12 12"><path d="M2 6h7M6 3l3 3-3 3" stroke="#fff" stroke-width="1.8" fill="none"/></svg></div>
  </article>

  <div class="abs band"></div>
  <h2 class="abs section-title" style="top:1472px">Latest Collections</h2>

  <div class="abs tab on" style="left:285px">KITCHENWARE</div>
  <div class="abs tab off" style="left:594px">Popular Products</div>
  <div class="abs tab-rule"></div>

  <div class="abs product" style="left:88px">
    <div class="photo" role="img" aria-label="Chef knife on a slate board" style="background:linear-gradient(135deg,#3a3c3f,#7d8286 55%,#2a2b2d)"></div>
    <div class="name">Lorem ipsum dolor sit amet</div>
    <div class="row"><span><i class="ico">$</i>89.00</span><span><i class="ico">&#9711;</i>Add to cart</span></div>
  </div>
  <div class="abs product" style="left:341px">
    <div class="photo" role="img" aria-label="Wooden spoons on a rustic table" style="background:linear-gradient(135deg,#6b4a37,#b56a4a 50%,#8c6a52)"></div>
    <div class="name">Lorem ipsum dolor sit amet</div>
    <div class="row"><span><i class="ico">$</i>59.00</span><span><i class="ico">&#9711;</i>Add to cart</span></div>
  </div>
  <div class="abs product" style="left:595px">
    <div class="photo" role="img" aria-label="Knife and chopped herbs on a cutting board" style="background:linear-gradient(135deg,#1b1d1f,#a7743f 50%,#1d1f21)"></div>
    <div class="name">Lorem ipsum dolor sit amet</div>
    <div class="row"><span><i class="ico">$</i>34.00</span><span><i class="ico">&#9711;</i>Add to cart</span></div>
  </div>
  <div class="abs product" style="left:848px">
    <div class="photo" role="img" aria-label="Steel saucepan with vegetables on white" style="background:linear-gradient(135deg,#ffffff,#e8e8e8 55%,#bdbdbd)"></div>
    <div class="name">Lorem ipsum dolor sit amet</div>
    <div class="row"><span><i class="ico">$</i>49.00</span><span><i class="ico">&#9711;</i>Add to cart</span></div>
  </div>

  <div class="abs pager">
    <span class="arrow">&#8249;</span><span>1</span><span>2</span><span class="on">3</span><span>4</span><span>5</span><span>6</span><span>7</span><span>8</span><span>9</span><span class="arrow">&#8250;</span>
  </div>

  <svg class="abs foot-tab" width="1172" height="62" viewBox="0 0 1172 62" aria-hidden="true">
    <path d="M0 62H1172V62H836C822 62 810 55 800 40L786 20C776 6 768 2 752 2H420C404 2 396 6 386 20L372 40C362 55 350 62 336 62H0Z" fill="#fff"/>
    <rect x="0" y="60" width="1172" height="2" fill="#fff"/>
  </svg>
  <div class="abs foot-brand">QUILLFERN<br>STORES</div>
  <div class="abs foot-rule"></div>
  <nav class="abs foot-nav">
    <a style="left:272px">HOME</a>
    <a style="left:352px">SHOP BY BRAND</a>
    <a style="left:494px">LATEST PROMOTION</a>
    <a style="left:657px">EVENTS</a>
    <a style="left:745px">NEWS</a>
    <a style="left:824px">CONTACT US</a>
  </nav>
  <div class="abs bar"><span>COPYRIGHT © 2018 QUILLFERN STORES ALL RIGHTS RESERVED.</span><span>TERMS OF USE I PRIVACY STATEMENT</span></div>

</div>
</body>
</html>
```